Revamp a website that sells books on machine learning and A.I

Hello I would like to create a minimalist concept to revamp this website:

www.quillvane.co.uk

We can change everything including the logo.

Somethings that I don't like:
- Generic images of people.
- Robot images.

The books are about the mathematics for machine learning and A.I and I would like for the website to have a blog as well as a scheduling tool, were people can book a call with me.

The scheduling tool, needs to have text and different tiers, for example 15 m free and 60 m 45 usd

Target Market(s)

university students and mathematics enthusiasts

Industry/Entity Type

machine learning, education, books, mathematics, A.I

Number of Pages Required

4 page

Requirements
Must have
• Landing Page, blog page, scheduling page, optimised conversion funnel
Should not have
• Arbitrary images from people or robots

```html
<!DOCTYPE html>
<html lang="en">
<head>
<meta charset="utf-8">
<title>Quillvane – Website Revamp Screens</title>
<link href="https://fonts.googleapis.com/css2?family=Inter:ital,wght@0,400;0,500;0,600;0,700;0,800;1,400;1,500&display=swap" rel="stylesheet">
<style>
:root{
  --red:#e04a3f;
  --green:#2e8b57;
  --yellow:#f1c15a;
  --ink:#1a1a1a;
  --muted:#555;
  --grey:#d9d9d9;
  --soft:#f4f4f4;
  --paper:#ffffff;
  --tint-pink:#fbe6e4;
  --tint-green:#e5f2ea;
  --tint-cream:#fbf1dc;
}
*{box-sizing:border-box;margin:0;padding:0}
html,body{width:1146px;height:1200px;overflow:hidden;background:var(--paper);font-family:'Inter',sans-serif;color:var(--ink)}
.canvas{position:relative;width:1146px;height:1200px}
.screen{position:absolute;transform-origin:0 0;transform:scale(.605);background:var(--paper);box-shadow:0 2px 10px rgba(0,0,0,.12);overflow:hidden}
.screen > *{position:absolute}
.page-long{width:463px;height:1608px}
.page-schedule{width:474px;height:338px;background:radial-gradient(circle at 15% 70%,var(--tint-green),transparent 45%),radial-gradient(circle at 85% 30%,var(--tint-pink),transparent 50%),var(--paper)}
.page-cart{width:479px;height:340px;background:radial-gradient(circle at 90% 40%,var(--tint-cream),transparent 50%),radial-gradient(circle at 10% 80%,var(--tint-green),transparent 45%),var(--paper)}
.wash{left:0;right:0;pointer-events:none}
/* header */
.brand{display:flex;align-items:center;gap:4px;font-weight:700;font-size:10px;color:var(--red)}
.brand-dot{width:9px;height:9px;border-radius:50%;background:var(--red)}
.nav{height:17px;border-radius:9px;background:var(--paper);box-shadow:0 1px 5px rgba(224,74,63,.25);display:flex;align-items:center;justify-content:center;gap:18px;font-size:5px;font-weight:500}
.nav .active{color:var(--red)}
.icons{display:flex;gap:6px}
.icon{width:20px;height:20px;border-radius:3px;display:flex;align-items:center;justify-content:center}
.icon.phone{background:var(--ink)}
.icon.cart{background:var(--red)}
/* common */
.center{left:0;right:0;text-align:center}
.pill{border:1px solid var(--red);border-radius:10px;font-size:8px;height:18px;display:flex;align-items:center;justify-content:center;background:var(--paper)}
.btn{display:flex;align-items:center;justify-content:center;color:#fff;font-weight:700;font-size:5px;border-radius:2px}
.btn.red{background:var(--red)}
.btn.green{background:var(--green)}
.btn.black{background:var(--ink)}
.red-text{color:var(--red)}
.tiny{font-size:5px;line-height:1.5;color:var(--muted)}
.body-text{font-size:5px;line-height:1.55;text-align:justify;color:#333}
.footer{left:0;right:0;bottom:0;background:var(--red);color:#fff;display:flex;justify-content:space-between;align-items:center;font-size:4px;padding:0 25px}
.footer b{font-size:4.5px}
.cover{border-radius:2px;box-shadow:0 2px 6px rgba(0,0,0,.2);background:linear-gradient(160deg,#f0b84a,#e9a83c 55%,#8fbf7a)}
.photo{background:linear-gradient(180deg,#d8d2cc,#9a918a)}
.ph{background:var(--grey)}
</style>
</head>
<body>
<main class="canvas">

<!-- Landing page -->
<section class="screen page-long" style="left:98px;top:112px;">
  <div class="wash" style="top:0;height:1425px;background:radial-gradient(circle at 80% 25%,var(--tint-pink),transparent 35%),radial-gradient(circle at 15% 40%,var(--tint-green),transparent 35%),radial-gradient(circle at 85% 70%,var(--tint-cream),transparent 35%),radial-gradient(circle at 20% 85%,var(--tint-pink),transparent 35%)"></div>
  <div class="brand" style="left:28px;top:30px"><span class="brand-dot"></span>Quillvane</div>
  <nav class="nav" style="left:150px;top:28px;width:162px"><span class="active">HOME</span><span>ABOUT</span><span>STORE</span><span>BLOG</span></nav>
  <div class="icons" style="left:387px;top:27px">
    <span class="icon phone"><svg width="11" height="11" viewBox="0 0 24 24"><path fill="#fff" d="M6.6 10.8a15 15 0 0 0 6.6 6.6l2.2-2.2c.3-.3.7-.4 1-.2 1.1.4 2.3.6 3.6.6.6 0 1 .4 1 1V20c0 .6-.4 1-1 1A17 17 0 0 1 3 4c0-.6.4-1 1-1h3.5c.6 0 1 .4 1 1 0 1.3.2 2.5.6 3.6.1.3 0 .7-.2 1z"/></svg></span>
    <span class="icon cart"><svg width="12" height="12" viewBox="0 0 24 24" fill="none" stroke="#fff" stroke-width="2"><path d="M2 3h3l2.5 12h11L21 7H6"/><circle cx="9" cy="19" r="1.5"/><circle cx="17" cy="19" r="1.5"/></svg></span>
  </div>

  <p class="center" style="top:82px;font-size:7px"><span style="border-bottom:1px solid var(--red)">Latest Release</span></p>
  <h1 class="center" style="top:107px;font-size:14px;font-weight:400;line-height:1.3">Beneath the Model<br><span class="red-text">Vol 2</span> - Calculus</h1>

  <svg style="left:170px;top:180px" width="60" height="60"><circle cx="30" cy="30" r="24" fill="none" stroke="var(--red)" stroke-width="7"/></svg>
  <div class="cover" style="left:82px;top:200px;width:123px;height:185px" role="img" aria-label="Cover of Beneath the Model Vol 2 – Calculus, illustrated yellow and green book"></div>
  <div style="left:258px;top:200px;width:132px">
    <p class="tiny">Calculus sits at the heart of model training, giving the tools needed to follow how functions change. Derivatives and integrals guide gradient steps, shape error rates and explain why a network learns. A steady grasp of calculus is the ground for real progress in these methods.</p>
    <p class="tiny" style="margin-top:8px;font-weight:700;color:var(--ink)">Start a lively walk through calculus for model building, where the steps become your guides in reading the inner logic of AI.</p>
    <p class="tiny" style="margin-top:8px;font-weight:700;color:var(--ink)">Tomas Verrow</p>
  </div>
  <div class="btn red" style="left:258px;top:365px;width:64px;height:18px">START READING</div>

  <div class="pill" style="left:190px;top:455px;width:83px">About Me</div>
  <h2 class="center" style="top:485px;font-size:28px;font-weight:500">Tomas Verrow</h2>
  <div class="photo" style="left:205px;top:560px;width:54px;height:63px" role="img" aria-label="Portrait photo of the author"></div>
  <p class="center" style="top:640px;font-size:6px;font-style:italic"><span style="border-bottom:1px solid var(--red)">A Mathematician and now a book writer</span></p>
  <p class="tiny" style="left:120px;top:663px;width:223px;text-align:center">I am a mathematician with over a decade of experience in building and shipping learning systems. My books are written in an easy style with humour. They are rich in practical uses, helping readers not only grasp the ideas but also see how they apply in the field of data science.</p>

  <div class="pill" style="left:174px;top:768px;width:116px">Customer Reviews</div>
  <div style="left:54px;top:823px;width:95px"><p style="font-size:6px;margin-bottom:6px">Ravi</p><p class="tiny" style="font-size:4px">"As a student new to the field without much linear algebra, this book was a real help. It starts from the basics and moves at a fair pace to set out core ideas..."</p></div>
  <div style="left:186px;top:823px;width:95px"><p style="font-size:6px;margin-bottom:6px">Owen Marsh</p><p class="tiny" style="font-size:4px">"...If you want a resource that blends breadth and depth so you can grasp the basics of linear algebra and then apply them to your own projects, stop here..."</p></div>
  <div style="left:318px;top:823px;width:95px"><p style="font-size:6px;margin-bottom:6px">Lia</p><p class="tiny" style="font-size:4px">"...The chatty tone of the book is a real strength. It feels less like a dry textbook and more like a novel. This approach puts the reader at ease, mainly when facing hard topics..."</p></div>

  <div class="pill" style="left:174px;top:980px;width:116px">There are 2 of them!</div>
  <div class="cover" style="left:97px;top:1048px;width:93px;height:142px" role="img" aria-label="Cover of Beneath the Model Vol 1 – Linear Algebra"></div>
  <div class="cover" style="left:263px;top:1048px;width:93px;height:142px" role="img" aria-label="Cover of Beneath the Model Vol 2 – Calculus"></div>
  <p style="left:60px;top:1200px;width:166px;text-align:center;font-size:6px;line-height:1.4">Beneath the Model<br><span class="red-text">Vol 1</span> - Linear Algebra EBOOK PDF</p>
  <p style="left:226px;top:1200px;width:166px;text-align:center;font-size:6px;line-height:1.4">Beneath the Model<br><span class="red-text">Vol 2</span> - Calculus EBOOK PDF</p>
  <p style="left:60px;top:1233px;width:166px;text-align:center;font-size:8px">7,50 €</p>
  <p style="left:226px;top:1233px;width:166px;text-align:center;font-size:8px">7,50 €</p>
  <div class="btn red" style="left:109px;top:1255px;width:70px;height:19px">ADD TO CART</div>
  <div class="btn green" style="left:275px;top:1255px;width:70px;height:19px">ADD TO CART</div>

  <div style="left:0;right:0;top:1425px;bottom:0;background:var(--red)"></div>
  <div style="left:68px;top:1322px;width:328px;height:185px;background:var(--paper);box-shadow:0 2px 8px rgba(0,0,0,.15)"></div>
  <h3 class="center" style="top:1357px;font-size:16px;font-weight:800;line-height:1.3"><span class="red-text">SUBSCRIBE</span><br>FOR A FREE CHAPTER!</h3>
  <div style="left:128px;top:1412px;width:207px;height:24px;border:1px solid #ccc;background:#f8f8f8"></div>
  <div class="btn green" style="left:199px;top:1455px;width:64px;height:18px">ADD TO CART</div>
  <p style="left:25px;top:1580px;font-size:4px;color:#fff">Copyright © 2023 All rights reserved by Quillvane</p>
  <p style="right:25px;top:1579px;font-size:4.5px;color:#fff;font-weight:700">LINK FOR CODE AND EXCERCISES</p>
</section>

<!-- Blog page -->
<section class="screen page-long" style="left:440px;top:112px;">
  <div class="wash" style="top:0;height:300px;background:radial-gradient(circle at 80% 10%,var(--tint-pink),transparent 40%),radial-gradient(circle at 10% 15%,var(--tint-green),transparent 35%)"></div>
  <div class="brand" style="left:28px;top:30px"><span class="brand-dot"></span>Quillvane</div>
  <nav class="nav" style="left:150px;top:28px;width:162px"><span>HOME</span><span>ABOUT</span><span>STORE</span><span class="active">BLOG</span></nav>
  <div class="icons" style="left:387px;top:27px">
    <span class="icon phone"><svg width="11" height="11" viewBox="0 0 24 24"><path fill="#fff" d="M6.6 10.8a15 15 0 0 0 6.6 6.6l2.2-2.2c.3-.3.7-.4 1-.2 1.1.4 2.3.6 3.6.6.6 0 1 .4 1 1V20c0 .6-.4 1-1 1A17 17 0 0 1 3 4c0-.6.4-1 1-1h3.5c.6 0 1 .4 1 1 0 1.3.2 2.5.6 3.6.1.3 0 .7-.2 1z"/></svg></span>
    <span class="icon cart"><svg width="12" height="12" viewBox="0 0 24 24" fill="none" stroke="#fff" stroke-width="2"><path d="M2 3h3l2.5 12h11L21 7H6"/><circle cx="9" cy="19" r="1.5"/><circle cx="17" cy="19" r="1.5"/></svg></span>
  </div>
  <p style="left:67px;top:79px;font-size:5px;color:var(--muted)">OCT 10, 2024</p>
  <h1 class="center" style="top:115px;font-size:14px;font-weight:400;line-height:1.3">Beneath the Model<br><span class="red-text">Vol 2</span> - Calculus</h1>
  <div style="left:67px;top:192px;width:328px">
    <p class="body-text">Lorem ipsum dolor sit amet consectetur. Suspendisse elementum ullamcorper vulputate quis rhoncus ac aliquet. Integer a tellus vitae mauris mi cursus donec ut. Id dictum sit elementum duis integer massa. Pulvinar neque metus eget at scelerisque a ipsum consectetur ut. Eu bibendum eu non tristique morbi erat suspendisse luctus elit. Cursus faucibus arcu a pretium tortor ultrices vulputate. In nisl consectetur eu accumsan. Ultrices volutpat id suscipit a montes ipsum quam pretium eget.</p>
    <p class="body-text" style="margin-top:6px">Id fermentum nunc tempus aenean ornare. Mauris id odio phasellus vestibulum iaculis a placerat ridiculus ac. Sagittis cursus ultrices molestie volutpat malesuada diam. Leo facilisis enim ullamcorper sollicitudin tellus morbi lorem. Nibh orci dignissim placerat ultricies imperdiet dui id. Scelerisque semper velit aliquam congue lectus integer. Neque proin quisque vestibulum sit diam id.</p>
    <p class="body-text" style="margin-top:6px">enim suscipit molestie tortor integer.<br>Tincidunt aliquet nulla facilisis eu. In eu et eget blandit habitant nulla vel volutpat. Id risus placerat tristique erat mi purus laoreet odio.</p>
  </div>
  <div class="ph" style="left:67px;top:367px;width:328px;height:140px" role="img" aria-label="Example figure one"></div>
  <p class="center" style="top:517px;font-size:4.5px;font-weight:600">EXAMPLE 1</p>
  <div class="ph" style="left:67px;top:531px;width:328px;height:139px" role="img" aria-label="Example figure two"></div>
  <p class="center" style="top:680px;font-size:4.5px;font-weight:600">EXAMPLE 1</p>
  <div style="left:67px;top:705px;width:188px">
    <p class="body-text">Lorem ipsum dolor sit amet consectetur. Suspendisse elementum ullamcorper vulputate quis rhoncus ac aliquet. Integer a tellus vitae mauris mi cursus donec ut. Id dictum sit elementum duis integer massa. Pulvinar neque metus eget at scelerisque a ipsum consectetur ut. Eu bibendum eu non tristique morbi erat suspendisse luctus elit. Cursus faucibus arcu a pretium tortor ultrices vulputate. In nisl consectetur eu accumsan.</p>
    <p class="body-text" style="margin-top:6px">Id fermentum nunc tempus aenean ornare. Mauris id odio phasellus vestibulum iaculis a placerat ridiculus ac. Sagittis cursus ultrices molestie volutpat malesuada diam. Leo facilisis enim ullamcorper sollicitudin tellus morbi lorem. Nibh orci dignissim placerat ultricies imperdiet dui id. Scelerisque semper velit aliquam congue lectus integer. Neque proin quisque vestibulum sit diam id. Viverra id urna massa pharetra enim imperdiet vehicula turpis vitae.</p>
    <p class="body-text" style="margin-top:6px">enim suscipit molestie tortor integer.<br>Tincidunt aliquet nulla facilisis eu. In eu et eget blandit habitant nulla vel volutpat. Id risus placerat tristique erat mi purus laoreet odio. Euismod vitae nec congue.</p>
  </div>
  <div class="ph" style="left:271px;top:705px;width:124px;height:111px" role="img" aria-label="Side figure"></div>
  <div class="ph" style="left:271px;top:844px;width:124px;height:111px" role="img" aria-label="Side figure"></div>
  <div style="left:67px;top:985px;width:328px">
    <p class="body-text">Lorem ipsum dolor sit amet consectetur. Suspendisse elementum ullamcorper vulputate quis rhoncus ac aliquet. Integer a tellus vitae mauris mi cursus donec ut. Id dictum sit elementum duis integer massa. Pulvinar neque metus eget at scelerisque a ipsum consectetur ut. Eu bibendum eu non tristique morbi erat suspendisse luctus elit. Cursus faucibus arcu a pretium tortor ultrices vulputate.</p>
    <p class="body-text" style="margin-top:6px">Id fermentum nunc tempus aenean ornare. Mauris id odio phasellus vestibulum iaculis a placerat ridiculus ac. Sagittis cursus ultrices molestie volutpat malesuada diam. Leo facilisis enim ullamcorper sollicitudin tellus morbi lorem. Nibh orci dignissim placerat ultricies imperdiet dui id. Scelerisque semper velit aliquam congue lectus integer.</p>
    <p class="body-text" style="margin-top:6px">enim suscipit molestie tortor integer.<br>Tincidunt aliquet nulla facilisis eu. In eu et eget blandit habitant nulla vel volutpat. Id risus placerat tristique erat mi purus laoreet odio.</p>
  </div>

  <div style="left:0;right:0;top:1190px;height:390px;background:var(--soft)"></div>
  <h2 class="center" style="top:1215px;font-size:15px;font-weight:400">Other Blogs</h2>
  <article style="left:55px;top:1270px;width:108px;height:200px;background:var(--paper);padding:6px">
    <div class="ph" style="height:70px"></div>
    <p style="font-size:3.5px;color:var(--red);margin-top:10px">Dec 4, 2024</p>
    <p style="font-size:6px;font-weight:700;margin-top:5px;line-height:1.2">Lorem ipsum dolor sit amet consectetur.</p>
    <p class="tiny" style="font-size:3.5px;margin-top:8px">Risus sed libero metus luctus risus. Pulvinar malesuada adipiscing commodo et fames. Est malesuada tortor dictumst in et tincidunt duis metus.</p>
    <p style="font-size:3.5px;color:var(--red);margin-top:3px">Read More ...</p>
  </article>
  <article style="left:177px;top:1270px;width:108px;height:200px;background:var(--paper);padding:6px">
    <div class="ph" style="height:70px"></div>
    <p style="font-size:3.5px;color:var(--red);margin-top:10px">Dec 4, 2024</p>
    <p style="font-size:6px;font-weight:700;margin-top:5px;line-height:1.2">Lorem ipsum dolor sit amet consectetur.</p>
    <p class="tiny" style="font-size:3.5px;margin-top:8px">Risus sed libero metus luctus risus. Pulvinar malesuada adipiscing commodo et fames. Est malesuada tortor dictumst in et tincidunt duis metus.</p>
    <p style="font-size:3.5px;color:var(--red);margin-top:3px">Read More ...</p>
  </article>
  <article style="left:299px;top:1270px;width:108px;height:200px;background:var(--paper);padding:6px">
    <div class="ph" style="height:70px"></div>
    <p style="font-size:3.5px;color:var(--red);margin-top:10px">Dec 4, 2024</p>
    <p style="font-size:6px;font-weight:700;margin-top:5px;line-height:1.2">Lorem ipsum dolor sit amet consectetur.</p>
    <p class="tiny" style="font-size:3.5px;margin-top:8px">Risus sed libero metus luctus risus. Pulvinar malesuada adipiscing commodo et fames. Est malesuada tortor dictumst in et tincidunt duis metus.</p>
    <p style="font-size:3.5px;color:var(--red);margin-top:3px">Read More ...</p>
  </article>
  <div class="btn red" style="left:191px;top:1495px;width:81px;height:20px;font-size:8px;font-weight:400">More Blogs</div>
  <div style="left:405px;top:1527px;width:30px;height:29px;background:var(--tint-pink);display:flex;align-items:center;justify-content:center"><svg width="14" height="10" viewBox="0 0 14 10"><path d="M1 8l6-6 6 6" fill="none" stroke="var(--ink)" stroke-width="2"/></svg></div>
  <div class="footer" style="height:28px"><span>Copyright © 2023 All rights reserved by Quillvane</span><b>Link For Code And Excercises</b></div>
</section>

<!-- Schedule page -->
<section class="screen page-schedule" style="left:764px;top:117px;">
  <div class="brand" style="left:30px;top:30px"><span class="brand-dot"></span>Quillvane</div>
  <nav class="nav" style="left:153px;top:28px;width:166px"><span>HOME</span><span>ABOUT</span><span>STORE</span><span>BLOG</span></nav>
  <div class="icons" style="left:395px;top:28px">
    <span class="icon phone"><svg width="11" height="11" viewBox="0 0 24 24"><path fill="#fff" d="M6.6 10.8a15 15 0 0 0 6.6 6.6l2.2-2.2c.3-.3.7-.4 1-.2 1.1.4 2.3.6 3.6.6.6 0 1 .4 1 1V20c0 .6-.4 1-1 1A17 17 0 0 1 3 4c0-.6.4-1 1-1h3.5c.6 0 1 .4 1 1 0 1.3.2 2.5.6 3.6.1.3 0 .7-.2 1z"/></svg></span>
    <span class="icon cart"><svg width="12" height="12" viewBox="0 0 24 24" fill="none" stroke="#fff" stroke-width="2"><path d="M2 3h3l2.5 12h11L21 7H6"/><circle cx="9" cy="19" r="1.5"/><circle cx="17" cy="19" r="1.5"/></svg></span>
  </div>
  <h1 class="center" style="top:87px;font-size:24px;font-weight:400;line-height:1.3">Schedule a <span class="red-text">Phone</span><br><span class="red-text">Call</span> with Me...</h1>
  <svg style="left:205px;top:148px" width="110" height="8"><path d="M2 6 Q55 0 108 3" fill="none" stroke="var(--red)" stroke-width="2.5" stroke-linecap="round"/></svg>
  <p style="left:85px;top:188px;width:88px;text-align:center;font-size:8px;color:var(--red)">15 Minutes</p>
  <div class="btn red" style="left:85px;top:205px;width:88px;height:22px;font-size:11px;font-weight:400">Free Call</div>
  <p class="tiny" style="left:85px;top:236px;width:88px;text-align:center;font-size:3.8px;line-height:1.3">Lorem ipsum dolor sit amet consectetur. Odio libero nulla ut velit magna sapien id.</p>
  <div class="photo" style="left:200px;top:182px;width:72px;height:72px;border-radius:50%;border:2px solid #ccc" role="img" aria-label="Portrait photo of the author"></div>
  <p style="left:298px;top:188px;width:89px;text-align:center;font-size:8px">60 Minutes</p>
  <div class="btn black" style="left:298px;top:205px;width:89px;height:22px;font-size:11px;font-weight:400">Paid Call $45</div>
  <p class="tiny" style="left:298px;top:236px;width:89px;text-align:center;font-size:3.8px;line-height:1.3">Lorem ipsum dolor sit amet consectetur. Odio libero nulla ut velit magna sapien id.</p>
  <div class="footer" style="height:30px"><span>Copyright © 2023 All rights reserved by Quillvane</span><b>Link For Code And Excercises</b></div>
</section>

<!-- Cart page -->
<section class="screen page-cart" style="left:765px;top:367px;">
  <div class="brand" style="left:32px;top:33px"><span class="brand-dot"></span>Quillvane</div>
  <nav class="nav" style="left:154px;top:29px;width:168px"><span>HOME</span><span>ABOUT</span><span>STORE</span><span>BLOG</span></nav>
  <div class="icons" style="left:400px;top:28px">
    <span class="icon phone"><svg width="11" height="11" viewBox="0 0 24 24"><path fill="#fff" d="M6.6 10.8a15 15 0 0 0 6.6 6.6l2.2-2.2c.3-.3.7-.4 1-.2 1.1.4 2.3.6 3.6.6.6 0 1 .4 1 1V20c0 .6-.4 1-1 1A17 17 0 0 1 3 4c0-.6.4-1 1-1h3.5c.6 0 1 .4 1 1 0 1.3.2 2.5.6 3.6.1.3 0 .7-.2 1z"/></svg></span>
    <span class="icon cart"><svg width="12" height="12" viewBox="0 0 24 24" fill="none" stroke="#fff" stroke-width="2"><path d="M2 3h3l2.5 12h11L21 7H6"/><circle cx="9" cy="19" r="1.5"/><circle cx="17" cy="19" r="1.5"/></svg></span>
  </div>
  <p style="left:46px;top:97px;font-size:6px">My Cart</p>
  <div style="left:33px;top:112px;width:253px;height:150px;background:var(--paper)"></div>
  <div class="cover" style="left:47px;top:125px;width:32px;height:46px" role="img" aria-label="Book cover thumbnail"></div>
  <p style="left:85px;top:133px;width:65px;font-size:4px;line-height:1.3">Beneath the Model Learning VOL 2 - Calculus EBOOK PDF</p>
  <p style="left:177px;top:133px;font-size:6px">–<span style="display:inline-block;width:7px;height:7px;border-radius:50%;background:var(--ink);margin:0 4px;vertical-align:middle"></span>+</p>
  <p style="left:235px;top:134px;font-size:4.5px">7,50</p>
  <div class="cover" style="left:47px;top:198px;width:32px;height:46px" role="img" aria-label="Book cover thumbnail"></div>
  <p style="left:85px;top:206px;width:65px;font-size:4px;line-height:1.3">Beneath the Model Learning VOL 2 - Calculus EBOOK PDF</p>
  <p style="left:177px;top:206px;font-size:6px">–<span style="display:inline-block;width:7px;height:7px;border-radius:50%;background:var(--ink);margin:0 4px;vertical-align:middle"></span>+</p>
  <p style="left:235px;top:207px;font-size:4.5px">7,50</p>
  <p style="left:316px;top:97px;font-size:6px">Order Summary</p>
  <div style="left:300px;top:111px;width:145px;height:151px;background:var(--yellow)"></div>
  <div style="left:313px;top:122px;width:116px;height:19px;background:var(--paper);font-size:5.5px;display:flex;justify-content:space-between;align-items:center;padding:0 6px"><span>Subtotal</span><span style="font-size:4.5px">15,00</span></div>
  <div style="left:313px;top:146px;width:116px;height:19px;background:var(--paper);font-size:5.5px;display:flex;align-items:center;padding:0 6px">Promo Code</div>
  <div style="left:313px;top:170px;width:116px;height:19px;background:var(--paper);font-size:5.5px;display:flex;align-items:center;padding:0 6px">Total</div>
  <div class="btn black" style="left:313px;top:201px;width:116px;height:20px;font-size:7px">CHECKOUT NOW</div>
  <p style="left:313px;top:228px;width:130px;text-align:center;font-size:3.5px">Secure Checkout</p>
  <div style="left:332px;top:274px;display:flex;gap:6px;align-items:center">
    <span style="width:6px;height:9px;background:#2a4a9a;border-radius:1px"></span>
    <span style="width:16px;height:9px;background:#bbb;border-radius:1px"></span>
    <span style="width:14px;height:9px;background:#1f3a8a;border-radius:1px"></span>
    <span style="width:14px;height:9px;background:#e8a33a;border-radius:1px"></span>
  </div>
  <div class="footer" style="height:29px"><span>Copyright © 2023 All rights reserved by Quillvane</span><b>Link For Code And Excercises</b></div>
</section>

<!-- Schedule page, second view -->
<section class="screen page-schedule" style="left:764px;top:620px;">
  <div class="brand" style="left:30px;top:30px"><span class="brand-dot"></span>Quillvane</div>
  <nav class="nav" style="left:153px;top:28px;width:166px"><span>HOME</span><span>ABOUT</span><span>STORE</span><span>BLOG</span></nav>
  <div class="icons" style="left:395px;top:28px">
    <span class="icon phone"><svg width="11" height="11" viewBox="0 0 24 24"><path fill="#fff" d="M6.6 10.8a15 15 0 0 0 6.6 6.6l2.2-2.2c.3-.3.7-.4 1-.2 1.1.4 2.3.6 3.6.6.6 0 1 .4 1 1V20c0 .6-.4 1-1 1A17 17 0 0 1 3 4c0-.6.4-1 1-1h3.5c.6 0 1 .4 1 1 0 1.3.2 2.5.6 3.6.1.3 0 .7-.2 1z"/></svg></span>
    <span class="icon cart"><svg width="12" height="12" viewBox="0 0 24 24" fill="none" stroke="#fff" stroke-width="2"><path d="M2 3h3l2.5 12h11L21 7H6"/><circle cx="9" cy="19" r="1.5"/><circle cx="17" cy="19" r="1.5"/></svg></span>
  </div>
  <h1 class="center" style="top:87px;font-size:24px;font-weight:400;line-height:1.3">Schedule a <span class="red-text">Phone</span><br><span class="red-text">Call</span> with Me...</h1>
  <svg style="left:205px;top:148px" width="110" height="8"><path d="M2 6 Q55 0 108 3" fill="none" stroke="var(--red)" stroke-width="2.5" stroke-linecap="round"/></svg>
  <p style="left:85px;top:188px;width:88px;text-align:center;font-size:8px;color:var(--red)">15 Minutes</p>
  <div class="btn red" style="left:85px;top:205px;width:88px;height:22px;font-size:11px;font-weight:400">Free Call</div>
  <p class="tiny" style="left:85px;top:236px;width:88px;text-align:center;font-size:3.8px;line-height:1.3">Lorem ipsum dolor sit amet consectetur. Odio libero nulla ut velit magna sapien id.</p>
  <div class="photo" style="left:200px;top:182px;width:72px;height:72px;border-radius:50%;border:2px solid #ccc" role="img" aria-label="Portrait photo of the author"></div>
  <p style="left:298px;top:188px;width:89px;text-align:center;font-size:8px">60 Minutes</p>
  <div class="btn black" style="left:298px;top:205px;width:89px;height:22px;font-size:11px;font-weight:400">Paid Call $45</div>
  <p class="tiny" style="left:298px;top:236px;width:89px;text-align:center;font-size:3.8px;line-height:1.3">Lorem ipsum dolor sit amet consectetur. Odio libero nulla ut velit magna sapien id.</p>
  <div class="footer" style="height:30px"><span>Copyright © 2023 All rights reserved by Quillvane</span><b>Link For Code And Excercises</b></div>
</section>

<!-- Cart page, second view -->
<section class="screen page-cart" style="left:765px;top:871px;">
  <div class="brand" style="left:32px;top:33px"><span class="brand-dot"></span>Quillvane</div>
  <nav class="nav" style="left:154px;top:29px;width:168px"><span>HOME</span><span>ABOUT</span><span>STORE</span><span>BLOG</span></nav>
  <div class="icons" style="left:400px;top:28px">
    <span class="icon phone"><svg width="11" height="11" viewBox="0 0 24 24"><path fill="#fff" d="M6.6 10.8a15 15 0 0 0 6.6 6.6l2.2-2.2c.3-.3.7-.4 1-.2 1.1.4 2.3.6 3.6.6.6 0 1 .4 1 1V20c0 .6-.4 1-1 1A17 17 0 0 1 3 4c0-.6.4-1 1-1h3.5c.6 0 1 .4 1 1 0 1.3.2 2.5.6 3.6.1.3 0 .7-.2 1z"/></svg></span>
    <span class="icon cart"><svg width="12" height="12" viewBox="0 0 24 24" fill="none" stroke="#fff" stroke-width="2"><path d="M2 3h3l2.5 12h11L21 7H6"/><circle cx="9" cy="19" r="1.5"/><circle cx="17" cy="19" r="1.5"/></svg></span>
  </div>
  <p style="left:46px;top:97px;font-size:6px">My Cart</p>
  <div style="left:33px;top:112px;width:253px;height:150px;background:var(--paper)"></div>
  <div class="cover" style="left:47px;top:125px;width:32px;height:46px" role="img" aria-label="Book cover thumbnail"></div>
  <p style="left:85px;top:133px;width:65px;font-size:4px;line-height:1.3">Beneath the Model Learning VOL 2 - Calculus EBOOK PDF</p>
  <p style="left:177px;top:133px;font-size:6px">–<span style="display:inline-block;width:7px;height:7px;border-radius:50%;background:var(--ink);margin:0 4px;vertical-align:middle"></span>+</p>
  <p style="left:235px;top:134px;font-size:4.5px">7,50</p>
  <div class="cover" style="left:47px;top:198px;width:32px;height:46px" role="img" aria-label="Book cover thumbnail"></div>
  <p style="left:85px;top:206px;width:65px;font-size:4px;line-height:1.3">Beneath the Model Learning VOL 2 - Calculus EBOOK PDF</p>
  <p style="left:177px;top:206px;font-size:6px">–<span style="display:inline-block;width:7px;height:7px;border-radius:50%;background:var(--ink);margin:0 4px;vertical-align:middle"></span>+</p>
  <p style="left:235px;top:207px;font-size:4.5px">7,50</p>
  <p style="left:316px;top:97px;font-size:6px">Order Summary</p>
  <div style="left:300px;top:111px;width:145px;height:151px;background:var(--yellow)"></div>
  <div style="left:313px;top:122px;width:116px;height:19px;background:var(--paper);font-size:5.5px;display:flex;justify-content:space-between;align-items:center;padding:0 6px"><span>Subtotal</span><span style="font-size:4.5px">15,00</span></div>
  <div style="left:313px;top:146px;width:116px;height:19px;background:var(--paper);font-size:5.5px;display:flex;align-items:center;padding:0 6px">Promo Code</div>
  <div style="left:313px;top:170px;width:116px;height:19px;background:var(--paper);font-size:5.5px;display:flex;align-items:center;padding:0 6px">Total</div>
  <div class="btn black" style="left:313px;top:201px;width:116px;height:20px;font-size:7px">CHECKOUT NOW</div>
  <p style="left:313px;top:228px;width:130px;text-align:center;font-size:3.5px">Secure Checkout</p>
  <div style="left:332px;top:274px;display:flex;gap:6px;align-items:center">
    <span style="width:6px;height:9px;background:#2a4a9a;border-radius:1px"></span>
    <span style="width:16px;height:9px;background:#bbb;border-radius:1px"></span>
    <span style="width:14px;height:9px;background:#1f3a8a;border-radius:1px"></span>
    <span style="width:14px;height:9px;background:#e8a33a;border-radius:1px"></span>
  </div>
  <div class="footer" style="height:29px"><span>Copyright © 2023 All rights reserved by Quillvane</span><b>Link For Code And Excercises</b></div>
</section>

</main>
</body>
</html>
```